Velorin Pain Management (this is the name of our clinics)

We are a medical group who will open a few new offices to see patients who are interested in medical cannabis therapy. We want to express this in a poster or a life size stand-alone cardboard ad to inform patients that 'this is the place'. We may also want to use the electronic ad on an e-billboard. We will not dispense any of the cannabis on sit but we will see patients and issue prescriptions and user cards, and we will align those patients with a federal grower who will deliver the meds (cannabis oil) to their place. We dont have a logo yet, so we want that as well.

Target Market(s)

Patients with repetitive strain injuries and other chronic pains, or post traumatic stress disorder from the military of victims of traumatic accidents or assaults.

Industry/Entity Type

Medical And Science

Requirements
Must have
• A poster showing a patient in clinic setting with our clinic name (Velorin Pain Management)

```html
<!DOCTYPE html>
<html lang="en">
<head>
<meta charset="utf-8">
<title>Velorin Pain Management – Medical Cannabis Therapy</title>
<link rel="stylesheet" href="https://fonts.googleapis.com/css2?family=Archivo+Black&family=Playfair+Display:wght@900&display=swap">
<style>
  :root {
    --red: #ec2a14;
    --red-shadow: rgba(90, 20, 10, 0.35);
    --ink: #2b2622;
    --green: #17895a;
    --teal: #1a9f8c;
    --square-red: #e4241b;
    --paper: #ffffff;
    --leaf-light: #c9ef7a;
    --leaf-mid: #7cc62c;
    --leaf-deep: #3f8a14;
  }
  * { margin: 0; padding: 0; box-sizing: border-box; }
  html, body { width: 800px; height: 1200px; overflow: hidden; background: var(--paper); }
  .poster { position: relative; width: 800px; height: 1200px; overflow: hidden; background: var(--paper); }

  .clinic-photo {
    position: absolute; left: 0; top: 0; width: 800px; height: 828px;
    background:
      radial-gradient(ellipse 260px 150px at 150px 640px, rgba(214,166,134,0.85), rgba(214,166,134,0) 70%),
      radial-gradient(ellipse 200px 160px at 640px 640px, rgba(225,226,232,0.95), rgba(225,226,232,0) 75%),
      linear-gradient(180deg, #f7f9f6 0%, #eef2ee 45%, #e6e6e0 72%, #d9d6cf 100%);
  }
  .clinic-photo-margin { position: absolute; left: 0; top: 0; width: 152px; height: 372px; background: var(--paper); }
  .leaf-top {
    position: absolute; left: 440px; top: 0; width: 360px; height: 372px;
    background: radial-gradient(ellipse 320px 300px at 300px 120px, var(--leaf-mid), var(--leaf-light) 55%, rgba(230,245,200,0) 85%);
  }
  .leaf-mid {
    position: absolute; left: 400px; top: 828px; width: 400px; height: 220px;
    background: radial-gradient(ellipse 380px 220px at 330px 110px, var(--leaf-mid), var(--leaf-light) 55%, rgba(240,250,220,0) 90%);
  }
  .leaf-bottom {
    position: absolute; left: 150px; top: 1160px; width: 650px; height: 40px;
    background: linear-gradient(90deg, #f3f6ea 0%, var(--leaf-light) 45%, var(--leaf-mid) 70%, var(--leaf-deep) 100%);
  }
  .logo-band { position: absolute; left: 150px; top: 1048px; width: 650px; height: 112px; background: var(--paper); }

  .headline { position: absolute; left: 0; top: 0; font-family: "Archivo Black", Arial, sans-serif; color: var(--red); text-shadow: 3px 4px 4px var(--red-shadow); }
  .headline span { position: absolute; white-space: nowrap; letter-spacing: -0.05em; line-height: 1; }
  .h-intro { left: 74px; top: 58px; font-size: 56px; }
  .h-post { left: 72px; top: 128px; font-size: 86px; }
  .h-stress { left: 60px; top: 186px; font-size: 150px; letter-spacing: -0.06em; }
  .h-and { left: 548px; top: 240px; font-size: 86px; }
  .h-repetitive { left: 68px; top: 330px; font-size: 80px; }
  .h-injuries { left: 66px; top: 410px; font-size: 134px; }

  .service-tag { position: absolute; left: 300px; top: 584px; font-family: "Playfair Display", Georgia, serif; font-weight: 900; color: var(--ink); text-align: center; line-height: 1; }
  .service-tag .line-1 { display: block; font-size: 27px; }
  .service-tag .line-2 { display: block; font-size: 40px; margin-top: 2px; }

  .therapy-title { position: absolute; left: 0; width: 832px; top: 858px; text-align: center; font-family: "Playfair Display", Georgia, serif; font-weight: 900; color: var(--green); line-height: 1; text-shadow: 2px 3px 3px rgba(0,0,0,0.3); }
  .therapy-title .line-1 { display: block; font-size: 46px; letter-spacing: -0.01em; }
  .therapy-title .line-2 { display: block; font-size: 64px; margin-top: 4px; }

  .clinic-name { position: absolute; left: 182px; top: 1076px; display: flex; align-items: center; gap: 14px; }
  .clinic-name .mark { width: 30px; height: 30px; background: var(--square-red); }
  .clinic-name .name { font-family: "Archivo Black", Arial, sans-serif; font-size: 29px; color: var(--teal); white-space: nowrap; }
</style>
</head>
<body>
<main class="poster">
  <div class="clinic-photo" role="img" aria-label="Photo of a patient's clasped hands across a desk from a doctor writing on a clipboard in a bright clinic"></div>
  <div class="clinic-photo-margin"></div>
  <div class="leaf-top" role="img" aria-label="Close-up photo of a green cannabis leaf"></div>
  <div class="leaf-mid" role="img" aria-label="Close-up photo of a green cannabis leaf"></div>
  <div class="logo-band"></div>
  <div class="leaf-bottom" role="img" aria-label="Strip of green cannabis leaf photo"></div>

  <h1 class="headline">
    <span class="h-intro">A Place for</span>
    <span class="h-post">Post Traumatic</span>
    <span class="h-stress">Stress</span>
    <span class="h-and">and</span>
    <span class="h-repetitive">Repetitive strain</span>
    <span class="h-injuries">Injuries</span>
  </h1>

  <p class="service-tag"><span class="line-1">Consultation &amp;</span><span class="line-2">Healing</span></p>

  <h2 class="therapy-title"><span class="line-1">MEDICAL CANNABIS</span><span class="line-2">Theraphy</span></h2>

  <div class="clinic-name"><span class="mark"></span><span class="name">Velorin Pain Management</span></div>
</main>
</body>
</html>
```